PowerPoint Design Project

We are looking for a corporate presentation design (example content provided on approximately 30 slides).

The design will be a corporate design for our brand: GVRU
Continental Voyage Planners Union
For brand colours, requirements and logo look at: www.gvru-sample.org/media
or check the attached documents. We need to incorporate logo and brand but we are happy to refresh the palette. Attached please also find designs and colour palette of our new website-presentation should complement these.

You are also free to use photos from events some of which can be found here:
http://www.socialpage-example.com/pages/Continental-Voyage-Planners-Union/507194362810935?sk=photos_stream

Most important:
-PROFESSIONAL AUDIENCE-PROFESSIONAL DESIGN
-SIMPLE (see example our homepage in attachment)
-ADDED SIMPLE ANIMATIONS

-DESIGN TO BE DONE ON THE EXAMPLE PRESENTATION BUT TO BE RE-USABLE FOR OTHER PRESENTATIONS
Updates

Hi, we have just uploaded our corporate social media icons which could be added on contact/end slide and on the welcome slide.

Hi all, 

-I uploaded a new high res version of the map which can be included in your designs (feel free to change colour scheme)
-Also amended upload of the Google + social media icon

Reason: I am looking forward to seeing a couple more designs. Please try including some suggested animations.

Target Market(s)

Presentation will be B2B and most audience are representatives of various companies in the tourism industry (tour operators, tourist boards, hotels )

Industry/Entity Type

Events

Requirements
Must have
• sleek graphics design
Nice to have
• animations

```html
<!DOCTYPE html>
<html lang="en">
<head>
<meta charset="utf-8">
<title>GVRU – Quick Facts</title>
<link rel="stylesheet" href="https://fonts.googleapis.com/css2?family=Bebas+Neue&family=Open+Sans:wght@400;700&display=swap">
<style>
  :root {
    --page-bg: #f2f2f2;
    --navy: #1c2955;
    --navy-deep: #0e1733;
    --card: #c6d9f1;
    --card-edge: #e8f0fa;
    --figure: #7f9cc4;
    --chart: #8db3e2;
    --ink: #404040;
    --ink-strong: #333333;
    --white: #ffffff;
  }
  * { box-sizing: border-box; margin: 0; padding: 0; }
  html, body { width: 1200px; height: 900px; overflow: hidden; background: var(--page-bg); }
  .slide { position: relative; width: 1200px; height: 900px; background: var(--page-bg); font-family: "Open Sans", sans-serif; color: var(--ink); }

  .title-band { position: absolute; left: 12px; top: 15px; width: 1173px; height: 141px; background: var(--navy); }
  .slide-title { position: absolute; left: 198px; top: 38px; font-family: "Bebas Neue", sans-serif; font-size: 92px; line-height: 1; letter-spacing: 1px; color: var(--white); }

  .brand-tab { position: absolute; left: 30px; top: 8px; width: 145px; height: 177px; }
  .brand-tab svg { position: absolute; inset: 0; }
  .brand-name { position: absolute; left: 0; width: 145px; top: 70px; text-align: center; font-family: "Open Sans", sans-serif; font-size: 22px; font-weight: 400; color: var(--white); letter-spacing: 1px; }

  .timeline-rail { position: absolute; left: 592px; top: 272px; width: 18px; height: 628px; background: var(--card); border-radius: 9px; }
  .timeline-node { position: absolute; left: 580px; width: 42px; height: 42px; border-radius: 50%; background: var(--card); }

  .pointer { position: absolute; width: 26px; height: 40px; }

  .fact-card { position: absolute; background: var(--card); border: 1.5px solid var(--card-edge); border-radius: 12px; }
  .fact-text { position: absolute; font-size: 37px; line-height: 1.27; color: var(--ink); }
  .fact-text strong { font-weight: 700; color: var(--ink-strong); }

  .founded { left: 48px; top: 262px; width: 485px; height: 99px; }
  .founded .fact-text { left: 20px; top: 24px; }

  .reach { left: 48px; top: 406px; width: 485px; height: 416px; }
  .reach .fact-text { left: 16px; top: 20px; }
  .world-map { position: absolute; left: 22px; top: 154px; width: 432px; height: 234px; border-radius: 40px; background: radial-gradient(ellipse at 50% 50%, #8aa6cc 0%, #a7bfe0 60%, var(--card) 100%); }

  .membership { left: 672px; top: 262px; width: 485px; height: 278px; }
  .membership .fact-text { left: 28px; top: 16px; font-size: 42px; }
  .member-group { position: absolute; left: 66px; top: 75px; width: 343px; height: 196px; border-radius: 60px 60px 0 0; background: linear-gradient(180deg, #9ab3d5 0%, var(--figure) 55%); }

  .purchasing { left: 672px; top: 595px; width: 485px; height: 230px; }
  .purchasing .fact-text { left: 16px; top: 18px; font-size: 42px; line-height: 1.3; }
  .growth-wedge { position: absolute; left: 0; top: 0; }
</style>
</head>
<body>
<main class="slide">
  <div class="title-band"></div>
  <div class="brand-tab">
    <svg width="145" height="177" viewBox="0 0 145 177" aria-hidden="true">
      <polygon points="0,0 145,0 145,152 0,177" fill="var(--navy-deep)"/>
    </svg>
    <span class="brand-name">GVRU</span>
  </div>
  <h1 class="slide-title">Quick Facts</h1>

  <div class="timeline-rail"></div>
  <div class="timeline-node" style="top:295px"></div>
  <div class="timeline-node" style="top:439px"></div>
  <div class="timeline-node" style="top:629px"></div>

  <svg class="pointer" style="left:540px; top:296px" viewBox="0 0 26 40" aria-hidden="true"><polygon points="0,0 26,20 0,40" fill="var(--card)"/></svg>
  <svg class="pointer" style="left:540px; top:440px" viewBox="0 0 26 40" aria-hidden="true"><polygon points="0,0 26,20 0,40" fill="var(--card)"/></svg>
  <svg class="pointer" style="left:640px; top:296px" viewBox="0 0 26 40" aria-hidden="true"><polygon points="26,0 0,20 26,40" fill="var(--card)"/></svg>
  <svg class="pointer" style="left:640px; top:630px" viewBox="0 0 26 40" aria-hidden="true"><polygon points="26,0 0,20 26,40" fill="var(--card)"/></svg>

  <section class="fact-card founded">
    <p class="fact-text">Established since <strong>1989</strong></p>
  </section>

  <section class="fact-card reach">
    <p class="fact-text">Members located in <strong>35</strong><br>countries worldwide</p>
    <div class="world-map" role="img" aria-label="World map silhouette showing member countries"></div>
  </section>

  <section class="fact-card membership">
    <p class="fact-text"><strong>600</strong> Members</p>
    <div class="member-group" role="img" aria-label="Silhouettes of a group of members"></div>
  </section>

  <section class="fact-card purchasing">
    <svg class="growth-wedge" width="485" height="230" viewBox="0 0 485 230" aria-hidden="true">
      <polygon points="34,215 461,90 461,215" fill="var(--chart)"/>
    </svg>
    <p class="fact-text"><strong>€5.5bn</strong> in product<br>purchasing</p>
  </section>
</main>
</body>
</html>
```